Fitness Centre/Personal Trainer Business Card

We need a business card design for a company based in Singapore called 'Vigor Summit'.

We are a team of Personal Trainers and we are planning to open our new training facility.

This design will also be printed/painted on the walls in our gym.

We are a new breed of personal trainers who take fitness seriously and holistically. We do not merely train our clients to be big and muscular.

We believe in wholeness. In our opinion, fitness should include: strength, speed, flexibility, mobility, stamina & agility. These are what we train for. Of course, nutrition/diet is key.

We use fitness tools such as kettlebells, QLV, Pylometric boxes, battling ropes, clubbells, medicine balls, bulgarian bags etc - functional and non-bulky tools.

I currently have a Facebook page 'Vigor Summit SG' which shows a logo of a kettlebell. But my business focus has since changed.

Services provided:
- Kettlebell Sport Preparation
- Calisthenics Training
- Corrective Exercises
- Sports Strength & Conditioning
- 28 days Weight Loss Program
- Myofascial Rehab Therapy
- Sports/Thai Massage

Main colors for the design should be BLACK & YELLOW. We envision a design which is able to protray the holistic view we take on fitness. Also it should somewhat appeal to the ladies and not intimidate them.

Target Market(s)

People between 18-35 years old. Students and working class alike.

Industry/Entity Type

Training

Requirements
Must have
• Name: Marcus Oleander Pryce
Fitness Coach
Corrective Exercise Specialist
M: +65 9372 6058
E: marcus@sgvigorsummit-example.com

Double-sided please.
Nice to have
• "What is your vigor summit?"

```html
<!DOCTYPE html>
<html lang="en">
<head>
<meta charset="UTF-8">
<title>Vigor Summit – Business Card</title>
<link rel="stylesheet" href="https://fonts.googleapis.com/css2?family=Roboto+Condensed:ital,wght@0,300;0,400;0,700;1,300;1,700;1,900&display=swap">
<style>
  :root {
    --card-yellow: #f5d300;
    --shade-yellow: #dcbb00;
    --tagline-yellow: #e2c200;
    --ink: #231f20;
  }
  html, body {
    margin: 0;
    padding: 0;
    width: 1200px;
    height: 667px;
    overflow: hidden;
    background: var(--card-yellow);
  }
  .card {
    position: relative;
    width: 1200px;
    height: 667px;
    overflow: hidden;
    background: var(--card-yellow);
    font-family: "Roboto Condensed", "Arial Narrow", sans-serif;
    color: var(--ink);
  }
  .athlete-art {
    position: absolute;
    left: 0;
    top: 0;
    width: 1200px;
    height: 667px;
  }
  .tagline {
    position: absolute;
    left: -4px;
    bottom: -26px;
    margin: 0;
    font-size: 102px;
    font-weight: 900;
    font-style: italic;
    letter-spacing: 1px;
    line-height: 1;
    white-space: nowrap;
    text-transform: uppercase;
    color: var(--tagline-yellow);
    transform: scaleX(0.98);
    transform-origin: left bottom;
  }
  .services {
    position: absolute;
    right: 39px;
    top: 49px;
    margin: 0;
    padding: 0;
    list-style: none;
    text-align: right;
  }
  .services li {
    font-size: 36px;
    font-weight: 700;
    font-style: italic;
    line-height: 58px;
    letter-spacing: -0.2px;
  }
  .contact-block {
    position: absolute;
    left: 51px;
    top: 229px;
  }
  .coach-name {
    margin: 0;
    font-size: 45px;
    font-weight: 700;
    line-height: 52px;
    letter-spacing: 0.2px;
  }
  .coach-role {
    margin: 0;
    font-size: 33px;
    font-weight: 300;
    font-style: italic;
    line-height: 45px;
  }
  .contact-list {
    margin: 78px 0 0;
    padding: 0;
    list-style: none;
  }
  .contact-list li {
    font-size: 34px;
    line-height: 45px;
    white-space: nowrap;
  }
  .contact-phone { font-weight: 700; }
  .contact-email { font-weight: 400; }
  .contact-email .label { font-weight: 700; margin-right: 12px; }
</style>
</head>
<body>
  <main class="card">
    <svg class="athlete-art" viewBox="0 0 1200 667" role="img" aria-label="Faint silhouette of an athlete doing a suspension-strap exercise">
      <defs>
        <linearGradient id="athleteShade" x1="1" y1="0" x2="0" y2="1">
          <stop offset="0" stop-color="#e4c400" stop-opacity="0.55"/>
          <stop offset="1" stop-color="#dcbb00" stop-opacity="0.8"/>
        </linearGradient>
      </defs>
      <path d="M740 0 L800 0 L1190 250 L1180 330 L1060 390 L880 470 L700 560 L600 640 L540 620 L560 530 L720 450 L930 330 L1030 250 Z" fill="url(#athleteShade)"/>
    </svg>

    <p class="tagline">What is your vigor summit?</p>

    <ul class="services">
      <li>Kettlebell Sport Preparation</li>
      <li>Calisthenics Training</li>
      <li>Corrective Exercises</li>
      <li>Sports Strength &amp; Conditioning</li>
      <li>28 days Weight Loss Program</li>
      <li>Myofascial Rehab Therapy</li>
      <li>Sports/Thai Massage</li>
    </ul>

    <section class="contact-block">
      <h1 class="coach-name">Marcus Oleander Pryce</h1>
      <p class="coach-role">Fitness Coach</p>
      <p class="coach-role">Corrective Exercise Specialist</p>
      <ul class="contact-list">
        <li class="contact-phone">M: +65 9372 6058</li>
        <li class="contact-email"><span class="label">E:</span>marcus@sgvigorsummit-example.com</li>
      </ul>
    </section>
  </main>
</body>
</html>
```